Dinewell - Slate App Design Project

I have a Slate app that serves as a restaurant reservation system. The design that i currently have is very basic apple design. I am looking for it to have a much more professional appeal.

Please review the attached document which contains all of the screen shots for the app.
Updates

This Project has now been Guaranteed.  I look forward to reviewing your designs.

Brent

Reason: I am extending my deadline because i just changed this contest to guaranteed and have received a ton more "acceptances" because of it and I want to give those designers a chance to submit a design.

Target Market(s)

restaurant owners

Industry/Entity Type

Restaurant

Requirements
Must have
• On the seating chart i am changing the feature that shows the tables highlighted and instead would like that replace with a badge. So the list of wait staff across the top of the seating chart would instead have a number next to their name and would correspond with the badge on the table to determine their section.

So for example:
Ada would have a number 1 in front of her name and tables 18, 19, 20, and 31 would have a little badge in the upper right hand corner with the number "1" inside the badge.
Uma would have a number 2 in front of her name and tables 6, 7, and 11 would have a little badge in the upper right hand corner with the number " 2" inside the badge.
Nora would have a number 3 in front of her name and tables 12, 13, 27, 28, 29, and 30 would have a little badge in the upper right hand corner with the number " 3" inside the badge.

The names on the top will all be ONE color

Also, i would like an icon developed to replace the "C" you see next to some of the people's name in the reservation and waitlist slots. Also, i would like a better looking "check mark".

```html
<!DOCTYPE html>
<html lang="en">
<head>
<meta charset="utf-8">
<title>Dinewell – Calendar</title>
<link rel="stylesheet" href="https://fonts.googleapis.com/css2?family=Arimo:wght@400;700&family=Open+Sans:wght@300;400;600&display=swap">
<style>
:root{
  --page:#ffffff;
  --statusbar:#000000;
  --nav-top:#f4f5f7;
  --nav-bottom:#c9ccd2;
  --nav-line:#7d828c;
  --ink:#1d1f24;
  --cal-cell-top:#e9eaed;
  --cal-cell-bottom:#c9cbd0;
  --cal-line:#9fa2a8;
  --cal-num:#3a3f4a;
  --cal-muted:#8c8f96;
  --select-top:#3f97f0;
  --select-bottom:#1162d2;
  --panel:#5b6178;
  --panel-line:#6d7389;
  --panel-shadow:#4a5066;
  --pill-top:#ffffff;
  --pill-bottom:#dcdde0;
  --time-top:#36a4f7;
  --time-bottom:#0a78de;
  --accent:#1877d6;
  --label:#3c3f44;
  --stripe-top:#e4e4e6;
  --stripe-mid:#f6f6f7;
  --stripe-bottom:#dadadc;
  --brand:#9a9a9c;
}
*{box-sizing:border-box;margin:0;padding:0}
html,body{width:1200px;height:1000px;overflow:hidden;background:var(--page)}
body{position:relative;font-family:"Arimo",Helvetica,Arial,sans-serif}
.screen{position:absolute;left:0;top:50px;width:1200px;height:900px;overflow:hidden}

.status-bar{position:absolute;left:0;top:0;width:1200px;height:22px;background:var(--statusbar);color:#fff;font-size:15px;font-weight:700}
.status-bar .device{position:absolute;left:4px;top:2px}
.status-bar .wifi{position:absolute;left:46px;top:3px}
.status-bar .clock{position:absolute;left:0;width:1200px;text-align:center;top:2px}
.status-bar .battery{position:absolute;right:6px;top:2px;display:flex;align-items:center;gap:4px}

.nav-bar{position:absolute;left:0;top:22px;width:1200px;height:53px;background:linear-gradient(var(--nav-top),var(--nav-bottom));border-bottom:1px solid var(--nav-line)}
.nav-bar .title{position:absolute;left:0;width:1200px;top:16px;text-align:center;font-size:17px;font-weight:700;color:var(--ink)}
.home-button{position:absolute;left:8px;top:9px;width:63px;height:33px;border-radius:5px;border:1px solid #4b5058;background:linear-gradient(#a7acb4,#6d737c);color:#fff;font-size:14px;font-weight:700;text-align:center;line-height:31px;text-shadow:0 -1px 0 #3c4047}

.sidebar{position:absolute;left:0;top:76px;width:380px;height:824px;background:#e5e5e7;border-right:4px solid #c9cacd}
.calendar{position:absolute;left:0;top:0;width:380px;height:324px;background:linear-gradient(#f2f2f4,#d8d9dc);box-shadow:0 3px 6px rgba(0,0,0,.35)}
.calendar .month{position:absolute;left:0;width:380px;top:20px;text-align:center;font-size:24px;font-weight:700;color:#3d4250}
.calendar .arrow{position:absolute;top:24px}
.calendar .arrow.prev{left:22px}
.calendar .arrow.next{left:344px}
.weekdays{position:absolute;left:4px;top:50px;display:grid;grid-template-columns:repeat(7,54px);font-size:11px;color:#4a4e58;text-align:center}
.days{position:absolute;left:4px;top:65px;display:grid;grid-template-columns:repeat(7,54px);grid-auto-rows:51.6px;border-top:1px solid var(--cal-line)}
.day{background:linear-gradient(var(--cal-cell-top),var(--cal-cell-bottom));border-right:1px solid var(--cal-line);border-bottom:1px solid var(--cal-line);font-size:24px;font-weight:700;color:var(--cal-num);display:flex;align-items:center;justify-content:center}
.day.outside{color:var(--cal-muted)}
.day.selected{background:linear-gradient(var(--select-top),var(--select-bottom));color:#fff;border:2px solid #0a3f8f}

.brand-area{position:absolute;left:0;top:324px;width:376px;height:500px;background:linear-gradient(var(--stripe-top),var(--stripe-mid) 45%,var(--stripe-bottom))}
.brand-name{position:absolute;left:0;width:376px;top:176px;text-align:center;font-family:"Open Sans",Helvetica,Arial,sans-serif;font-weight:300;font-size:68px;letter-spacing:-1px;color:var(--brand)}

.slots{position:absolute;left:384px;top:76px;width:816px;height:824px;background:var(--panel);box-shadow:inset 3px 0 4px var(--panel-shadow)}
.slot-grid{position:absolute;left:0;top:15px;width:816px}
.slot-row{height:61px;border-bottom:1px solid var(--panel-line);position:relative}
.slot-row:last-child{border-bottom:none}
.slot{position:absolute;top:14px;width:363px;height:33px;border-radius:6px;background:linear-gradient(var(--pill-top),var(--pill-bottom));box-shadow:0 1px 2px rgba(0,0,0,.45);font-family:"Open Sans",Helvetica,Arial,sans-serif;overflow:hidden}
.slot.left{left:29px}
.slot.right{left:429px}
.slot .time{position:absolute;left:0;top:0;width:100px;height:33px;background:linear-gradient(var(--time-top),var(--time-bottom));color:#fff;font-size:17px;font-weight:600;line-height:33px;text-align:center}
.slot .time small{font-size:11px;font-weight:600;margin-left:2px}
.slot .count{position:absolute;left:100px;width:102px;text-align:center;top:0;line-height:33px;font-size:17px;color:var(--accent)}
.slot .size{position:absolute;left:226px;width:66px;text-align:center;top:0;line-height:33px;font-size:17px;color:var(--label)}
.slot .add{position:absolute;left:323px;top:4px}
</style>
</head>
<body>
<div class="screen">
  <div class="status-bar">
    <span class="device">Slate</span>
    <svg class="wifi" width="18" height="14" viewBox="0 0 18 14"><path d="M9 13 L5.5 9.2 A5 5 0 0 1 12.5 9.2 Z" fill="#fff"/><path d="M2.8 6.6 A9 9 0 0 1 15.2 6.6" stroke="#fff" stroke-width="2" fill="none"/><path d="M0.6 4 A12 12 0 0 1 17.4 4" stroke="#fff" stroke-width="2" fill="none"/></svg>
    <span class="clock">12:13 PM</span>
    <span class="battery">25%
      <svg width="26" height="13" viewBox="0 0 26 13"><rect x="0.5" y="0.5" width="22" height="12" rx="2" fill="none" stroke="#fff"/><rect x="2" y="2" width="5" height="9" fill="#fff"/><rect x="23" y="4" width="2.5" height="5" fill="#fff"/></svg>
    </span>
  </div>

  <div class="nav-bar">
    <div class="home-button">Home</div>
    <div class="title">Calendar</div>
  </div>

  <aside class="sidebar">
    <div class="calendar">
      <svg class="arrow prev" width="18" height="18" viewBox="0 0 18 18"><path d="M16 1 L2 9 L16 17 Z" fill="#2e323b"/></svg>
      <div class="month">November 2012</div>
      <svg class="arrow next" width="18" height="18" viewBox="0 0 18 18"><path d="M2 1 L16 9 L2 17 Z" fill="#2e323b"/></svg>
      <div class="weekdays"><span>Sun</span><span>Mon</span><span>Tue</span><span>Wed</span><span>Thu</span><span>Fri</span><span>Sat</span></div>
      <div class="days">
        <div class="day outside">28</div><div class="day outside">29</div><div class="day outside">30</div><div class="day outside">31</div><div class="day">1</div><div class="day selected">2</div><div class="day">3</div>
        <div class="day">4</div><div class="day">5</div><div class="day">6</div><div class="day">7</div><div class="day">8</div><div class="day">9</div><div class="day">10</div>
        <div class="day">11</div><div class="day">12</div><div class="day">13</div><div class="day">14</div><div class="day">15</div><div class="day">16</div><div class="day">17</div>
        <div class="day">18</div><div class="day">19</div><div class="day">20</div><div class="day">21</div><div class="day">22</div><div class="day">23</div><div class="day">24</div>
        <div class="day">25</div><div class="day">26</div><div class="day">27</div><div class="day">28</div><div class="day">29</div><div class="day">30</div><div class="day outside">1</div>
      </div>
    </div>
    <div class="brand-area" role="img" aria-label="Light grey diagonal pinstripe texture behind the restaurant name">
      <div class="brand-name">Dinewell</div>
    </div>
  </aside>

  <main class="slots">
    <div class="slot-grid">
      <div class="slot-row"><div class="slot left"><div class="time">12:00<small>PM</small></div><div class="count">0/10</div><div class="size">Size</div><svg class="add" width="26" height="26" viewBox="0 0 26 26"><circle cx="13" cy="13" r="12" fill="#fff" stroke="#c0c4ca"/><circle cx="13" cy="13" r="10.5" fill="#1a7fe0"/><path d="M13 7.5 V18.5 M7.5 13 H18.5" stroke="#fff" stroke-width="2.6"/></svg></div><div class="slot right"><div class="time">12:00<small>PM</small></div><div class="count">0/10</div><div class="size">Size</div><svg class="add" width="26" height="26" viewBox="0 0 26 26"><circle cx="13" cy="13" r="12" fill="#fff" stroke="#c0c4ca"/><circle cx="13" cy="13" r="10.5" fill="#1a7fe0"/><path d="M13 7.5 V18.5 M7.5 13 H18.5" stroke="#fff" stroke-width="2.6"/></svg></div></div>
      <div class="slot-row"><div class="slot left"><div class="time">12:00<small>PM</small></div><div class="count">0/10</div><div class="size">Size</div><svg class="add" width="26" height="26" viewBox="0 0 26 26"><circle cx="13" cy="13" r="12" fill="#fff" stroke="#c0c4ca"/><circle cx="13" cy="13" r="10.5" fill="#1a7fe0"/><path d="M13 7.5 V18.5 M7.5 13 H18.5" stroke="#fff" stroke-width="2.6"/></svg></div><div class="slot right"><div class="time">12:00<small>PM</small></div><div class="count">0/10</div><div class="size">Size</div><svg class="add" width="26" height="26" viewBox="0 0 26 26"><circle cx="13" cy="13" r="12" fill="#fff" stroke="#c0c4ca"/><circle cx="13" cy="13" r="10.5" fill="#1a7fe0"/><path d="M13 7.5 V18.5 M7.5 13 H18.5" stroke="#fff" stroke-width="2.6"/></svg></div></div>
      <div class="slot-row"><div class="slot left"><div class="time">12:00<small>PM</small></div><div class="count">0/10</div><div class="size">Size</div><svg class="add" width="26" height="26" viewBox="0 0 26 26"><circle cx="13" cy="13" r="12" fill="#fff" stroke="#c0c4ca"/><circle cx="13" cy="13" r="10.5" fill="#1a7fe0"/><path d="M13 7.5 V18.5 M7.5 13 H18.5" stroke="#fff" stroke-width="2.6"/></svg></div><div class="slot right"><div class="time">12:00<small>PM</small></div><div class="count">0/10</div><div class="size">Size</div><svg class="add" width="26" height="26" viewBox="0 0 26 26"><circle cx="13" cy="13" r="12" fill="#fff" stroke="#c0c4ca"/><circle cx="13" cy="13" r="10.5" fill="#1a7fe0"/><path d="M13 7.5 V18.5 M7.5 13 H18.5" stroke="#fff" stroke-width="2.6"/></svg></div></div>
      <div class="slot-row"><div class="slot left"><div class="time">12:00<small>PM</small></div><div class="count">0/10</div><div class="size">Size</div><svg class="add" width="26" height="26" viewBox="0 0 26 26"><circle cx="13" cy="13" r="12" fill="#fff" stroke="#c0c4ca"/><circle cx="13" cy="13" r="10.5" fill="#1a7fe0"/><path d="M13 7.5 V18.5 M7.5 13 H18.5" stroke="#fff" stroke-width="2.6"/></svg></div><div class="slot right"><div class="time">12:00<small>PM</small></div><div class="count">0/10</div><div class="size">Size</div><svg class="add" width="26" height="26" viewBox="0 0 26 26"><circle cx="13" cy="13" r="12" fill="#fff" stroke="#c0c4ca"/><circle cx="13" cy="13" r="10.5" fill="#1a7fe0"/><path d="M13 7.5 V18.5 M7.5 13 H18.5" stroke="#fff" stroke-width="2.6"/></svg></div></div>
      <div class="slot-row"><div class="slot left"><div class="time">12:00<small>PM</small></div><div class="count">0/10</div><div class="size">Size</div><svg class="add" width="26" height="26" viewBox="0 0 26 26"><circle cx="13" cy="13" r="12" fill="#fff" stroke="#c0c4ca"/><circle cx="13" cy="13" r="10.5" fill="#1a7fe0"/><path d="M13 7.5 V18.5 M7.5 13 H18.5" stroke="#fff" stroke-width="2.6"/></svg></div><div class="slot right"><div class="time">12:00<small>PM</small></div><div class="count">0/10</div><div class="size">Size</div><svg class="add" width="26" height="26" viewBox="0 0 26 26"><circle cx="13" cy="13" r="12" fill="#fff" stroke="#c0c4ca"/><circle cx="13" cy="13" r="10.5" fill="#1a7fe0"/><path d="M13 7.5 V18.5 M7.5 13 H18.5" stroke="#fff" stroke-width="2.6"/></svg></div></div>
      <div class="slot-row"><div class="slot left"><div class="time">12:00<small>PM</small></div><div class="count">0/10</div><div class="size">Size</div><svg class="add" width="26" height="26" viewBox="0 0 26 26"><circle cx="13" cy="13" r="12" fill="#fff" stroke="#c0c4ca"/><circle cx="13" cy="13" r="10.5" fill="#1a7fe0"/><path d="M13 7.5 V18.5 M7.5 13 H18.5" stroke="#fff" stroke-width="2.6"/></svg></div><div class="slot right"><div class="time">12:00<small>PM</small></div><div class="count">0/10</div><div class="size">Size</div><svg class="add" width="26" height="26" viewBox="0 0 26 26"><circle cx="13" cy="13" r="12" fill="#fff" stroke="#c0c4ca"/><circle cx="13" cy="13" r="10.5" fill="#1a7fe0"/><path d="M13 7.5 V18.5 M7.5 13 H18.5" stroke="#fff" stroke-width="2.6"/></svg></div></div>
      <div class="slot-row"><div class="slot left"><div class="time">12:00<small>PM</small></div><div class="count">0/10</div><div class="size">Size</div><svg class="add" width="26" height="26" viewBox="0 0 26 26"><circle cx="13" cy="13" r="12" fill="#fff" stroke="#c0c4ca"/><circle cx="13" cy="13" r="10.5" fill="#1a7fe0"/><path d="M13 7.5 V18.5 M7.5 13 H18.5" stroke="#fff" stroke-width="2.6"/></svg></div><div class="slot right"><div class="time">12:00<small>PM</small></div><div class="count">0/10</div><div class="size">Size</div><svg class="add" width="26" height="26" viewBox="0 0 26 26"><circle cx="13" cy="13" r="12" fill="#fff" stroke="#c0c4ca"/><circle cx="13" cy="13" r="10.5" fill="#1a7fe0"/><path d="M13 7.5 V18.5 M7.5 13 H18.5" stroke="#fff" stroke-width="2.6"/></svg></div></div>
      <div class="slot-row"><div class="slot left"><div class="time">12:00<small>PM</small></div><div class="count">0/10</div><div class="size">Size</div><svg class="add" width="26" height="26" viewBox="0 0 26 26"><circle cx="13" cy="13" r="12" fill="#fff" stroke="#c0c4ca"/><circle cx="13" cy="13" r="10.5" fill="#1a7fe0"/><path d="M13 7.5 V18.5 M7.5 13 H18.5" stroke="#fff" stroke-width="2.6"/></svg></div><div class="slot right"><div class="time">12:00<small>PM</small></div><div class="count">0/10</div><div class="size">Size</div><svg class="add" width="26" height="26" viewBox="0 0 26 26"><circle cx="13" cy="13" r="12" fill="#fff" stroke="#c0c4ca"/><circle cx="13" cy="13" r="10.5" fill="#1a7fe0"/><path d="M13 7.5 V18.5 M7.5 13 H18.5" stroke="#fff" stroke-width="2.6"/></svg></div></div>
      <div class="slot-row"><div class="slot left"><div class="time">12:00<small>PM</small></div><div class="count">0/10</div><div class="size">Size</div><svg class="add" width="26" height="26" viewBox="0 0 26 26"><circle cx="13" cy="13" r="12" fill="#fff" stroke="#c0c4ca"/><circle cx="13" cy="13" r="10.5" fill="#1a7fe0"/><path d="M13 7.5 V18.5 M7.5 13 H18.5" stroke="#fff" stroke-width="2.6"/></svg></div><div class="slot right"><div class="time">12:00<small>PM</small></div><div class="count">0/10</div><div class="size">Size</div><svg class="add" width="26" height="26" viewBox="0 0 26 26"><circle cx="13" cy="13" r="12" fill="#fff" stroke="#c0c4ca"/><circle cx="13" cy="13" r="10.5" fill="#1a7fe0"/><path d="M13 7.5 V18.5 M7.5 13 H18.5" stroke="#fff" stroke-width="2.6"/></svg></div></div>
      <div class="slot-row"><div class="slot left"><div class="time">12:00<small>PM</small></div><div class="count">0/10</div><div class="size">Size</div><svg class="add" width="26" height="26" viewBox="0 0 26 26"><circle cx="13" cy="13" r="12" fill="#fff" stroke="#c0c4ca"/><circle cx="13" cy="13" r="10.5" fill="#1a7fe0"/><path d="M13 7.5 V18.5 M7.5 13 H18.5" stroke="#fff" stroke-width="2.6"/></svg></div><div class="slot right"><div class="time">12:00<small>PM</small></div><div class="count">0/10</div><div class="size">Size</div><svg class="add" width="26" height="26" viewBox="0 0 26 26"><circle cx="13" cy="13" r="12" fill="#fff" stroke="#c0c4ca"/><circle cx="13" cy="13" r="10.5" fill="#1a7fe0"/><path d="M13 7.5 V18.5 M7.5 13 H18.5" stroke="#fff" stroke-width="2.6"/></svg></div></div>
      <div class="slot-row"><div class="slot left"><div class="time">12:00<small>PM</small></div><div class="count">0/10</div><div class="size">Size</div><svg class="add" width="26" height="26" viewBox="0 0 26 26"><circle cx="13" cy="13" r="12" fill="#fff" stroke="#c0c4ca"/><circle cx="13" cy="13" r="10.5" fill="#1a7fe0"/><path d="M13 7.5 V18.5 M7.5 13 H18.5" stroke="#fff" stroke-width="2.6"/></svg></div><div class="slot right"><div class="time">12:00<small>PM</small></div><div class="count">0/10</div><div class="size">Size</div><svg class="add" width="26" height="26" viewBox="0 0 26 26"><circle cx="13" cy="13" r="12" fill="#fff" stroke="#c0c4ca"/><circle cx="13" cy="13" r="10.5" fill="#1a7fe0"/><path d="M13 7.5 V18.5 M7.5 13 H18.5" stroke="#fff" stroke-width="2.6"/></svg></div></div>
      <div class="slot-row"><div class="slot left"><div class="time">12:00<small>PM</small></div><div class="count">0/10</div><div class="size">Size</div><svg class="add" width="26" height="26" viewBox="0 0 26 26"><circle cx="13" cy="13" r="12" fill="#fff" stroke="#c0c4ca"/><circle cx="13" cy="13" r="10.5" fill="#1a7fe0"/><path d="M13 7.5 V18.5 M7.5 13 H18.5" stroke="#fff" stroke-width="2.6"/></svg></div><div class="slot right"><div class="time">12:00<small>PM</small></div><div class="count">0/10</div><div class="size">Size</div><svg class="add" width="26" height="26" viewBox="0 0 26 26"><circle cx="13" cy="13" r="12" fill="#fff" stroke="#c0c4ca"/><circle cx="13" cy="13" r="10.5" fill="#1a7fe0"/><path d="M13 7.5 V18.5 M7.5 13 H18.5" stroke="#fff" stroke-width="2.6"/></svg></div></div>
      <div class="slot-row"><div class="slot left"><div class="time">12:00<small>PM</small></div><div class="count">0/10</div><div class="size">Size</div><svg class="add" width="26" height="26" viewBox="0 0 26 26"><circle cx="13" cy="13" r="12" fill="#fff" stroke="#c0c4ca"/><circle cx="13" cy="13" r="10.5" fill="#1a7fe0"/><path d="M13 7.5 V18.5 M7.5 13 H18.5" stroke="#fff" stroke-width="2.6"/></svg></div><div class="slot right"><div class="time">12:00<small>PM</small></div><div class="count">0/10</div><div class="size">Size</div><svg class="add" width="26" height="26" viewBox="0 0 26 26"><circle cx="13" cy="13" r="12" fill="#fff" stroke="#c0c4ca"/><circle cx="13" cy="13" r="10.5" fill="#1a7fe0"/><path d="M13 7.5 V18.5 M7.5 13 H18.5" stroke="#fff" stroke-width="2.6"/></svg></div></div>
    </div>
  </main>
</div>
</body>
</html>
```